stationary for a modern hotel
Venmiro Hotels
Project: stationary for a modern hotel
stationary for a modern hotel - Hospitality Industry
Creative Brief
Use same font as used in my logo
anything that can go very well with my logo
Simple
Tundeyemi Okafordike
G.M
Venmiro Hotels Plot 318,Adebanjo-Ekwueme Way,Garki District Abuja Nigeria
tunde@venmirohotels.com
www.venmirohotels.com

```html
<!DOCTYPE html>
<html lang="en">
<head>
<meta charset="utf-8">
<title>Venmiro Hotels — Business Card</title>
<link href="https://fonts.googleapis.com/css2?family=Cinzel:wght@500&family=Open+Sans:ital,wght@0,400;1,400&display=swap" rel="stylesheet">
<style>
  :root {
    --backdrop: #e9e6e2;
    --card-white: #ffffff;
    --brand-red: #b5121b;
    --brand-red-dark: #7d0a10;
    --brand-red-light: #d42a2f;
    --brand-gold: #9a6a3c;
    --ink-grey: #6b6b6b;
    --on-red: #ffffff;
  }
  html, body {
    margin: 0;
    padding: 0;
    width: 1200px;
    height: 914px;
    overflow: hidden;
    background: var(--backdrop);
  }
  .canvas {
    position: relative;
    width: 1200px;
    height: 914px;
  }
  .business-card {
    position: absolute;
    left: 100px;
    top: 171px;
    width: 1000px;
    height: 572px;
    background: var(--card-white);
    overflow: hidden;
    box-shadow: 0 2px 10px rgba(0,0,0,0.12);
    font-family: "Open Sans", Arial, sans-serif;
  }
  .card-band {
    position: absolute;
    inset: 0;
    width: 100%;
    height: 100%;
  }
  .brand-name {
    position: absolute;
    left: 70px;
    top: 78px;
    margin: 0;
    font-family: "Cinzel", Georgia, serif;
    font-weight: 500;
    font-size: 46px;
    letter-spacing: 1px;
    color: var(--brand-gold);
    text-transform: uppercase;
  }
  .holder {
    position: absolute;
    left: 72px;
    top: 205px;
    color: var(--ink-grey);
  }
  .holder-name {
    margin: 0;
    font-size: 19px;
    font-style: italic;
  }
  .holder-role {
    margin: 4px 0 0;
    font-size: 16px;
  }
  .address {
    position: absolute;
    left: 72px;
    top: 300px;
    margin: 0;
    font-size: 13px;
    font-style: italic;
    color: var(--ink-grey);
  }
  .contact-list {
    position: absolute;
    left: 630px;
    top: 385px;
    margin: 0;
    padding: 0;
    list-style: none;
    color: var(--on-red);
    font-size: 15px;
  }
  .contact-list li {
    display: flex;
    align-items: center;
    gap: 10px;
    height: 34px;
  }
  .contact-icon {
    width: 20px;
    height: 20px;
    flex: none;
  }
</style>
</head>
<body>
<div class="canvas">
  <div class="business-card">
    <svg class="card-band" viewBox="0 0 1000 572" preserveAspectRatio="none" aria-hidden="true">
      <defs>
        <linearGradient id="bandGradient" x1="0" y1="0" x2="1" y2="1">
          <stop offset="0" stop-color="var(--brand-red-light)"/>
          <stop offset="1" stop-color="var(--brand-red)"/>
        </linearGradient>
      </defs>
      <path d="M0 330 C 260 360, 560 340, 1000 215 L1000 572 L0 572 Z" fill="var(--brand-red-dark)"/>
      <path d="M0 350 C 280 380, 580 350, 1000 240 L1000 572 L0 572 Z" fill="url(#bandGradient)"/>
      <path d="M0 372 C 300 395, 620 360, 1000 262" fill="none" stroke="var(--card-white)" stroke-width="3"/>
    </svg>

    <h1 class="brand-name">Venmiro Hotels</h1>

    <div class="holder">
      <p class="holder-name">Tundeyemi Okafordike</p>
      <p class="holder-role">G.M</p>
    </div>

    <p class="address" style="top:420px;color:var(--on-red);">Venmiro Hotels Plot 318,Adebanjo-Ekwueme Way,Garki District Abuja Nigeria</p>

    <ul class="contact-list">
      <li>
        <svg class="contact-icon" viewBox="0 0 20 20"><circle cx="10" cy="10" r="10" fill="var(--on-red)"/><path d="M7 5.5l2 2-1 1.2c.6 1.3 1.7 2.4 3 3l1.2-1 2 2-1.2 1.6c-3.5-.4-6.8-3.7-7.2-7.2z" fill="var(--brand-red)"/></svg>
        <span>+234 803 555 0142</span>
      </li>
      <li>
        <svg class="contact-icon" viewBox="0 0 20 20"><circle cx="10" cy="10" r="10" fill="var(--on-red)"/><path d="M7 5.5l2 2-1 1.2c.6 1.3 1.7 2.4 3 3l1.2-1 2 2-1.2 1.6c-3.5-.4-6.8-3.7-7.2-7.2z" fill="var(--brand-red)"/></svg>
        <span>+234 809 555 0176</span>
      </li>
      <li>
        <svg class="contact-icon" viewBox="0 0 20 20"><circle cx="10" cy="10" r="10" fill="var(--on-red)"/><rect x="5" y="6.5" width="10" height="7" fill="none" stroke="var(--brand-red)" stroke-width="1.3"/><path d="M5 6.5l5 4 5-4" fill="none" stroke="var(--brand-red)" stroke-width="1.3"/></svg>
        <span>tunde@venmirohotels.com</span>
      </li>
      <li>
        <svg class="contact-icon" viewBox="0 0 20 20"><circle cx="10" cy="10" r="10" fill="var(--on-red)"/><circle cx="10" cy="10" r="5" fill="none" stroke="var(--brand-red)" stroke-width="1.3"/><path d="M5 10h10M10 5c-2 2.8-2 7.2 0 10M10 5c2 2.8 2 7.2 0 10" fill="none" stroke="var(--brand-red)" stroke-width="1.1"/></svg>
        <span>www.venmirohotels.com</span>
      </li>
    </ul>
  </div>
</div>
</body>
</html>
```